Marnie Lux Business Card Design

I need a business card for my daughter. She has it all described in the file below. But it needs to be square in shape. http://www.marnielux.com is her web site

Target Market(s)

18-35 year old women

Industry/Entity Type

Fashion

Contact Information for Business Card

Please look at the attached file as it has all the details.

Requirements
Must have
• Please look at the attached file as it has all the details.
Nice to have
Should not have

```html
<!DOCTYPE html>
<html lang="en">
<head>
<meta charset="utf-8">
<title>Marnie Lux – Business Card</title>
<link rel="stylesheet" href="https://fonts.googleapis.com/css2?family=Libre+Baskerville&family=Dancing+Script:wght@500&family=Open+Sans:wght@700&family=Tinos&display=swap">
<style>
  :root {
    --page: #efece9;
    --lilac: #cfa8c3;
    --ink: #0b0b0b;
    --paper: #ffffff;
    --marble-dark: #0a0a0a;
    --marble-mid: #3a3a3a;
  }
  * { margin: 0; padding: 0; box-sizing: border-box; }
  html, body { width: 1200px; height: 960px; overflow: hidden; }
  body { background: var(--page); position: relative; }

  .card { position: absolute; width: 352px; height: 351px; }

  /* Front */
  .card--front { left: 226px; top: 305px; background: var(--lilac); }
  .marble {
    position: absolute; left: 12px; width: 327px;
    background: linear-gradient(135deg, var(--marble-dark) 0%, var(--marble-mid) 35%, var(--marble-dark) 55%, #555 80%, var(--marble-dark) 100%);
  }
  .marble--top { top: 11px; height: 114px; }
  .marble--bottom { top: 226px; height: 113px; }
  .brand-name {
    position: absolute; top: 134px; left: 0; width: 100%;
    text-align: center;
    font-family: "Libre Baskerville", serif;
    font-weight: 400;
    font-size: 34px; letter-spacing: 0.5px;
    color: var(--ink);
  }
  .brand-rule {
    position: absolute; top: 180px; left: 67px; width: 205px; height: 2px;
    background: var(--ink);
  }
  .tagline {
    position: absolute; top: 184px; left: 0; width: 100%;
    text-align: center;
    font-family: "Dancing Script", cursive;
    font-size: 25px; color: var(--ink);
  }

  /* Back */
  .card--back {
    left: 622px; top: 305px;
    background: var(--ink); padding: 11px 12px;
  }
  .back-inner { position: relative; width: 100%; height: 100%; background: var(--lilac); }
  .role-band {
    position: absolute; left: 8px; top: 8px; width: 311px; height: 37px;
    background: var(--ink); color: var(--paper);
    font-family: "Dancing Script", cursive; font-size: 17px;
    display: flex; align-items: center; justify-content: center;
    white-space: nowrap;
  }
  .contact-list { position: absolute; left: 21px; top: 64px; list-style: none; }
  .contact-list li {
    font-family: "Open Sans", sans-serif; font-weight: 700;
    font-size: 18px; color: var(--ink);
    height: 41px; line-height: 26px;
    white-space: nowrap;
  }
  .contact-list .marker { color: var(--paper); margin-right: 8px; }
  .links { position: absolute; left: 21px; top: 242px; }
  .links p {
    font-family: "Tinos", serif; font-size: 17px; color: var(--ink);
    height: 37px; white-space: nowrap;
  }
  .links .label { color: var(--paper); }
</style>
</head>
<body>
  <section class="card card--front">
    <div class="marble marble--top" role="img" aria-label="Black and white marble texture"></div>
    <h1 class="brand-name">MARNIE LUX</h1>
    <div class="brand-rule"></div>
    <p class="tagline">dressed with intent</p>
    <div class="marble marble--bottom" role="img" aria-label="Black and white marble texture"></div>
  </section>

  <section class="card card--back">
    <div class="back-inner">
      <div class="role-band">blogger &amp; vlogger // beauty-fashion-travel</div>
      <ul class="contact-list">
        <li><span class="marker">&lt;&gt;</span>picfeed.com/marnieluxxo</li>
        <li><span class="marker">&lt;&gt;</span>chatterly.com/marnieluxxo</li>
        <li><span class="marker">&lt;&gt;</span>@marnieluxxo</li>
        <li><span class="marker">&lt;&gt;</span>marnie@marnielux.com</li>
      </ul>
      <div class="links">
        <p><span class="label">BLOG:</span> marnielux.com</p>
        <p><span class="label">VIDEOS:</span> streamly.com/marnielux</p>
      </div>
    </div>
  </section>
</body>
</html>
```